Lumora Fabrix
A technical textile company
Lumora Fabrix -
Creative Brief
Professional
Ravi Kapoorji
Business Manager
117, Neel Kamal Residency Chandan Path , Moti Nagar Jaipur - 302049 Rajasthan , India
ravi.kapoorji@lumora-fabrix.example
www.lumora-fabrix.example
Skype : ravikelmora.. Also want - letter head - envelope - power point slide ( both first and regular pages) designs .
Address has to go in the back 117, Neel Kamal Residency Chandan Path , Moti Nagar Jaipur - 302049 Rajasthan , India

```html
<!DOCTYPE html>
<html lang="en">
<head>
<meta charset="utf-8">
<title>Lumora Fabrix – Business Cards</title>
<link href="https://fonts.googleapis.com/css2?family=Open+Sans:wght@400;600;700&display=swap" rel="stylesheet">
<style>
  :root {
    --page: #e9e6e1;
    --card: #ffffff;
    --card-shade: #eef0f2;
    --navy: #1d4f8c;
    --navy-dark: #163c6b;
    --orange: #e8742a;
    --ink: #2b2b2b;
    --muted: #6b6b6b;
    --rule: #b9c3cf;
  }
  * { box-sizing: border-box; margin: 0; padding: 0; }
  html, body { width: 1200px; height: 768px; overflow: hidden; }
  body {
    background: var(--page);
    font-family: "Open Sans", Arial, sans-serif;
    color: var(--ink);
    position: relative;
  }
  .card {
    position: absolute;
    width: 440px;
    height: 200px;
    border-radius: 16px;
    background: linear-gradient(135deg, var(--card) 0%, var(--card) 55%, var(--card-shade) 100%);
    box-shadow: 0 6px 14px rgba(0,0,0,0.18);
    overflow: hidden;
  }
  .card--front-a { left: 140px; top: 164px; }
  .card--front-b { left: 620px; top: 164px; }
  .card--back-a  { left: 140px; top: 404px; }
  .card--back-b  { left: 620px; top: 404px; }

  .swoosh { position: absolute; left: 0; bottom: 0; width: 440px; height: 70px; }

  .brand-name {
    position: absolute;
    font-weight: 700;
    color: var(--navy);
    letter-spacing: -0.3px;
    white-space: nowrap;
  }
  .tagline {
    position: absolute;
    font-size: 7px;
    color: var(--muted);
    letter-spacing: 1.6px;
    white-space: nowrap;
  }

  .person { position: absolute; }
  .person__name { font-size: 17px; font-weight: 400; color: var(--navy); line-height: 1.1; }
  .person__role { font-size: 8px; color: var(--muted); margin-bottom: 7px; }
  .person__line { font-size: 8px; line-height: 1.45; color: var(--ink); }
  .person__line b { color: var(--navy); font-weight: 700; }

  .web {
    position: absolute;
    font-size: 8px;
    white-space: nowrap;
  }
  .web--light { color: #fff; }
  .web--dark { color: var(--muted); letter-spacing: 0.8px; }

  .address { position: absolute; font-size: 8px; line-height: 1.45; color: var(--ink); }
  .vrule { position: absolute; width: 1px; background: var(--rule); }
</style>
</head>
<body>

<!-- Front, layout A -->
<section class="card card--front-a">
  <div class="brand-name" style="right:22px; top:52px; font-size:21px;">Lumora Fabrix</div>
  <div class="tagline" style="right:24px; top:80px;">engineered fabrics for industry</div>

  <div class="person" style="left:22px; top:78px;">
    <div class="person__name">Ravi Kapoorji</div>
    <div class="person__role">Business Manager</div>
    <div class="person__line"><b>Skype ID:</b> ravikelmora</div>
    <div class="person__line"><b>Cell:</b> +91 90000 12345</div>
    <div class="person__line"><b>Email:</b> ravi.kapoorji@lumora-fabrix.example</div>
  </div>

  <svg class="swoosh" viewBox="0 0 440 70" aria-hidden="true">
    <path d="M0 44 C120 20 260 30 440 40 L440 70 L0 70 Z" fill="var(--orange)"/>
    <path d="M0 50 C120 28 260 38 440 46 L440 70 L0 70 Z" fill="#ffffff"/>
    <path d="M0 58 C140 40 280 46 440 52 L440 70 L0 70 Z" fill="var(--navy)"/>
  </svg>
  <div class="web web--light" style="right:26px; bottom:5px;">www.lumora-fabrix.example</div>
</section>

<!-- Front, layout B -->
<section class="card card--front-b">
  <div class="brand-name" style="left:44px; top:16px; font-size:26px;">Lumora Fabrix</div>
  <div class="tagline" style="left:64px; top:50px;">engineered fabrics for industry</div>

  <div class="vrule" style="left:160px; top:80px; height:64px;"></div>
  <div class="person" style="left:172px; top:80px;">
    <div class="person__name">Ravi Kapoorji</div>
    <div class="person__role">Business Manager</div>
    <div class="person__line"><b>Skype ID:</b> ravikelmora</div>
    <div class="person__line"><b>Cell:</b> +91 90000 12345</div>
    <div class="person__line"><b>Email:</b> ravi.kapoorji@lumora-fabrix.example</div>
  </div>

  <svg class="swoosh" viewBox="0 0 440 70" aria-hidden="true">
    <path d="M0 30 C80 30 140 48 220 56 C300 62 380 60 440 58 L440 70 L0 70 Z" fill="var(--orange)"/>
    <path d="M0 36 C80 36 140 52 220 60 C300 65 380 64 440 62 L440 70 L0 70 Z" fill="#ffffff"/>
    <path d="M0 42 C80 42 140 56 220 63 C300 68 380 68 440 66 L440 70 L0 70 Z" fill="var(--navy)"/>
  </svg>
</section>

<!-- Back, layout A -->
<section class="card card--back-a">
  <div class="brand-name" style="left:0; right:0; top:58px; text-align:center; font-size:26px;">Lumora Fabrix</div>

  <div class="address" style="left:22px; top:140px;">
    117, Neel Kamal Residency<br>
    Chandan Path , Moti Nagar<br>
    Jaipur - 302049, Rajasthan, India
  </div>
</section>

<!-- Back, layout B -->
<section class="card card--back-b">
  <div class="brand-name" style="left:22px; top:76px; font-size:20px;">Lumora Fabrix</div>

  <div class="vrule" style="left:178px; top:52px; height:80px;"></div>
  <div class="address" style="left:190px; top:60px;">
    117, Neel Kamal Residency<br>
    Chandan Path<br>
    Moti Nagar<br>
    Jaipur - 302049<br>
    Rajasthan, India
  </div>

  <div class="web web--dark" style="left:0; right:0; bottom:10px; text-align:center;">www.lumora-fabrix.example</div>
</section>

</body>
</html>
```